AutoVelko an innovative way to connect sellers with car dealers

The idea is a site that connects consumers that want to sell thier cars with a dealer network that is ready to buy.

**I just added 9/26 a POSSIBLE logo. Dont feel obligated to use this or design off of it.

The first goal is to provide a place where people can SEAMLESSLY list their vechile for sale to a car dealership network. We are looking for people that want to get more for their car than trading it in allows but DONT want to go through the hassel of listing and selling their car on their own. The dont want to deal with people reaching out, showing the vechile, and the risk assocated with retailing a valuable item to the general public. That said these people dont want to just trade their car wholesale and buy retail. These are the people that that do to a place like RideBrant to sell their car directly. However RideBrant is just one dealer.

The second fuction of the site allows dealers to view the vechiles that have been listed especilaly the ones in thier market.

I would like to add that I am looking for real images. No cartoon or animation. Upmarket but friendly.

I have attached a detailed document to help.

Target Market(s)

People that want to sell cars and dealers that want to buy cars

Industry/Entity Type

Automotive

Requirements
Must have
• The pages listed in the document
Should not have
• No cartoon or animated images

```html
<!DOCTYPE html>
<html lang="en">
<head>
<meta charset="utf-8">
<title>AutoVelko – Sell Your Car Hassle Free</title>
<link href="https://fonts.googleapis.com/css2?family=Outfit:wght@400;500;600;700;800&display=swap" rel="stylesheet">
<style>
:root{
  --red:#cd1517;
  --red-dark:#8e0d0e;
  --ink:#111111;
  --muted:#555;
  --white:#ffffff;
  --soft-pink:#fbe6e8;
  --soft-blue:#eaf6fc;
  --panel:#f8f8f8;
}
*{margin:0;padding:0;box-sizing:border-box}
html,body{width:799px;height:1200px;overflow:hidden}
body{font-family:"Outfit",sans-serif;color:var(--ink);background:var(--white);position:relative}
.abs{position:absolute}

.topbar{left:0;top:0;width:799px;height:20px;background:var(--red)}
.social{display:flex;gap:7px;align-items:center}
.social span{width:9px;height:9px;border-radius:50%;background:var(--white);opacity:.9}
.social span.active{border-radius:2px;background:var(--white)}
.topbar .social{left:106px;top:6px}
.contact-top{top:5px;color:var(--white);font-size:7.5px;font-weight:600;display:flex;align-items:center;gap:4px}

.hero{left:0;top:20px;width:799px;height:360px}
.hero-photo{position:absolute;inset:0;background:linear-gradient(100deg,#2b2f35 0%,#4a4e55 30%,#6a6f78 55%,#3a4150 80%,#2a3140 100%)}
.hero-photo::after{content:"";position:absolute;inset:0;background:rgba(0,0,0,.35)}
.logo{color:var(--white);font-weight:700;letter-spacing:.3px}
.hero .logo{left:112px;top:11px;font-size:20px}
.nav{left:293px;top:12px;display:flex;gap:16px;align-items:center}
.nav a{color:var(--white);font-size:6.8px;font-weight:500;text-decoration:none;text-transform:uppercase}
.nav a.current{background:var(--red);padding:6px 8px}
.search{left:521px;top:12px;width:165px;height:19px;background:var(--white);border-radius:3px}
.search span{position:absolute;left:8px;top:5px;font-size:6.5px;color:#aaa}
.search i{position:absolute;right:1px;top:1px;width:19px;height:17px;background:#555;border-radius:2px}
.headline{left:0;width:799px;top:140px;text-align:center;color:var(--white);font-size:32px;font-weight:800;line-height:35px;text-transform:uppercase}
.headline em{font-style:normal;color:var(--red)}
.btn{display:flex;align-items:center;justify-content:center;font-size:7.5px;font-weight:500;text-transform:uppercase}
.hero .btn{left:346px;top:226px;width:106px;height:22px;background:var(--white);color:var(--ink);border-radius:2px}

.stat{top:457px;width:110px;height:100px;text-align:center}
.stat svg.blob{position:absolute;left:0;top:0}
.stat .icon{position:absolute;left:50%;transform:translateX(-50%);top:16px}
.stat b{position:absolute;left:0;width:100%;top:48px;color:var(--red);font-size:19px;font-weight:700}
.stat p{position:absolute;left:0;width:100%;top:71px;font-size:8.5px;color:var(--ink)}

.reviews{left:0;top:607px;width:799px;height:257px;background:var(--panel)}
.stars{left:144px;top:50px;display:flex;gap:3px;align-items:center;color:var(--red);font-size:7.5px}
.quote{left:144px;top:75px;width:360px;font-size:12.5px;line-height:16px;letter-spacing:.2px}
.divider{left:144px;top:170px;width:343px;height:1px;background:#e3e3e3}
.author{left:183px;top:184px}
.author h4{color:var(--red);font-size:8.5px;font-weight:600}
.author p{font-size:7px;margin-top:2px}
.dots{left:113px;top:110px;display:flex;flex-direction:column;gap:6px}
.dots span{width:6px;height:6px;border-radius:50%;border:1px solid #f2b8bb}
.dots span.on{border-color:var(--red)}

.cta-title{left:195px;top:913px;width:280px;text-align:center;font-size:19px;font-weight:700;line-height:23px;text-transform:uppercase}
.cta-btn{left:491px;top:927px;width:106px;height:22px;background:var(--red);color:var(--white)}

.footer{left:0;top:1005px;width:799px;height:175px;background:var(--red);color:var(--white)}
.footer .logo{left:99px;top:40px;font-size:19px}
.footer .about{left:99px;top:81px;width:120px;font-size:6.5px;line-height:8.8px}
.footer .more{left:99px;top:133px;font-size:6.5px;text-decoration:underline;opacity:.8}
.footer h3{font-size:10px;font-weight:600}
.col{top:42px}
.col ul{list-style:none;margin-top:11px}
.contact li{display:flex;gap:6px;font-size:7.3px;line-height:12px;margin-bottom:6px}
.contact svg{flex:none;margin-top:2px}
.links li{font-size:7.3px;margin-bottom:4.5px}
.links li:first-child{opacity:.55;text-decoration:underline}
.touch p{font-size:7.3px;line-height:9px;margin-top:13px}
.field{margin-top:13px;width:158px;border-bottom:1px solid rgba(255,255,255,.4);padding-bottom:5px;font-size:7.3px;display:flex;gap:6px;align-items:center}
.field i{width:9px;height:9px;border:1px solid var(--white);border-radius:50%}
.submit{margin-top:8px;width:64px;height:20px;background:var(--white);color:var(--ink)}
.bottom{left:0;top:1180px;width:799px;height:20px;background:var(--red-dark);color:var(--white)}
.bottom p{position:absolute;left:101px;top:5px;font-size:7.3px}
.bottom .social{position:absolute;left:638px;top:6px}
</style>
</head>
<body>

<header class="abs topbar">
  <div class="abs social"><span></span><span></span><span class="active"></span><span></span></div>
  <div class="abs contact-top" style="left:545px">
    <svg width="7" height="7" viewBox="0 0 10 10"><path d="M2 1l2 2-1 1.5a6 6 0 0 0 2.5 2.5L7 6l2 2-1.5 1.5C4.5 9 1 5.5.5 2.5z" fill="#fff"/></svg>555.214.0186</div>
  <div class="abs contact-top" style="left:616px">
    <svg width="8" height="7" viewBox="0 0 10 8"><rect x="0" y="0" width="10" height="8" rx="1" fill="#fff"/><path d="M0 1l5 3.5L10 1" stroke="#cd1517" fill="none"/></svg>sales@autovelko.com</div>
</header>

<section class="abs hero">
  <div class="hero-photo" role="img" aria-label="Photo of a smiling salesman and two women reviewing paperwork beside a car in a bright showroom"></div>
  <div class="abs logo">AUTOVELKO</div>
  <nav class="abs nav">
    <a class="current" href="#">Home</a><a href="#">What we do</a><a href="#">Sign in</a><a href="#">Dealership login</a>
  </nav>
  <div class="abs search"><span>Search by make, model, or keyword</span><i></i></div>
  <h1 class="abs headline"><em>Sell</em> your car<br>hassle <em>free</em></h1>
  <a class="abs btn">Sell your car now</a>
</section>

<div class="abs stat" style="left:132px">
  <svg class="blob" width="110" height="100" viewBox="0 0 110 100"><path d="M30 2C55-4 85 30 102 55c10 20-10 40-45 43C20 100 2 85 2 60 2 30 10 8 30 2z" fill="var(--soft-pink)"/></svg>
  <svg class="icon" width="34" height="24" viewBox="0 0 34 24" fill="none" stroke="#111" stroke-width="1.5"><path d="M4 12l4-8h14l4 8z"/><rect x="2" y="12" width="26" height="8" rx="2"/><circle cx="8" cy="16" r="1.5" fill="#cd1517" stroke="none"/><circle cx="22" cy="16" r="1.5" fill="#cd1517" stroke="none"/><path d="M20 4l2-3h8l3 7v8"/></svg>
  <b>1856</b><p>Vehicle in stock cars</p>
</div>
<div class="abs stat" style="left:265px;width:132px">
  <svg class="blob" width="132" height="100" viewBox="0 0 132 100"><path d="M60 2c15 0 25 25 50 40 25 20 20 40-20 44-40 6-80 8-85-15C0 50 40 2 60 2z" fill="var(--soft-blue)"/></svg>
  <svg class="icon" width="26" height="26" viewBox="0 0 26 26" fill="none" stroke="#111" stroke-width="1.3"><rect x="1" y="1" width="24" height="8" rx="1" fill="#cd1517" stroke="none"/><circle cx="7" cy="14" r="2.5"/><circle cx="19" cy="14" r="2.5"/><circle cx="13" cy="16" r="2.5"/><path d="M2 24c0-4 3-6 5-6M24 24c0-4-3-6-5-6M8 25c0-4 2-6 5-6s5 2 5 6"/></svg>
  <b>1485</b><p>Satisfied customers</p>
</div>
<div class="abs stat" style="left:424px;width:110px">
  <svg class="blob" width="110" height="100" viewBox="0 0 110 100"><path d="M8 2c20 5 40 10 70 8 25 0 25 15 15 30-8 15 10 30 6 40-5 12-60 0-80 12C5 100 0 70 2 40 3 20 0 0 8 2z" fill="var(--soft-pink)"/></svg>
  <svg class="icon" width="24" height="26" viewBox="0 0 24 26" fill="none" stroke="#111" stroke-width="1.3"><path d="M5 2h14v7a7 7 0 0 1-14 0z"/><path d="M5 4H1c0 4 2 6 4 6M19 4h4c0 4-2 6-4 6M12 16v4M7 24h10v-4H7z"/><path d="M12 5l1 2.5h2.5l-2 1.5 1 2.5-2.5-1.5-2.5 1.5 1-2.5-2-1.5H11z" fill="#cd1517" stroke="none"/></svg>
  <b>65+</b><p>Award achievement</p>
</div>
<div class="abs stat" style="left:555px;width:112px">
  <svg class="blob" width="112" height="100" viewBox="0 0 112 100"><path d="M45 2c20 5 50 10 62 20 8 10-5 30 0 55 2 20-20 25-50 15C30 90 5 95 2 75 0 55 20 45 30 35 40 20 30 0 45 2z" fill="var(--soft-blue)"/></svg>
  <svg class="icon" width="32" height="24" viewBox="0 0 32 24" fill="none" stroke="#111" stroke-width="1.3"><path d="M2 2v21h29V9L2 2"/><path d="M11 23v-8l12-2v10" /><rect x="18" y="17" width="4" height="4" fill="#cd1517" stroke="none"/><rect x="13" y="14" width="6" height="3" fill="#cd1517" stroke="none"/></svg>
  <b>10+</b><p>Total showroom</p>
</div>

<section class="abs reviews">
  <div class="abs stars">
    <svg width="62" height="10" viewBox="0 0 62 10" fill="#cd1517"><g id="s"><path d="M5 0l1.5 3.2 3.5.4-2.6 2.4.7 3.5L5 7.8 1.9 9.5l.7-3.5L0 3.6l3.5-.4z"/></g><use href="#s" x="12.5"/><use href="#s" x="25"/><use href="#s" x="37.5"/><path d="M55 0l1.5 3.2 3.5.4-2.6 2.4.7 3.5L55 7.8 51.9 9.5l.7-3.5L50 3.6l3.5-.4z" fill="none" stroke="#cd1517"/><path d="M55 0v7.8L51.9 9.5l.7-3.5L50 3.6l3.5-.4z"/></svg>
    <span style="margin-left:4px">4.5</span>
  </div>
  <p class="abs quote">Lorem Ipsum is simply dummy text of the printing and typesetting industry. Lorem Ipsum has been the industry's standard dummy text ever since the 1500s, when an unknown printer took a galley of type and scrambled it to make a type specimen book.</p>
  <div class="abs dots"><span></span><span></span><span class="on"></span><span></span></div>
  <div class="abs divider"></div>
  <svg class="abs" style="left:144px;top:184px" width="31" height="23" viewBox="0 0 31 23" fill="none" stroke="#cd1517" stroke-width="1"><path d="M10 1C4 5 1 10 1 15a6 6 0 1 0 12 0c0-4-3-6-7-5"/><path d="M26 1c-6 4-9 9-9 14a6 6 0 1 0 12 0c0-4-3-6-7-5"/></svg>
  <div class="abs author"><h4>Daniel Harlow</h4><p>Head of Data and AI at Trailnest</p></div>
  <svg class="abs" style="left:533px;top:68px" width="158" height="126" viewBox="0 0 158 126">
    <path d="M120 14c15-4 18 10 18 30 0 20 25 40 18 50-5 8-30 10-50 18L30 60C10 50-10 30 30 30 60 28 100 20 120 14z" fill="var(--red)"/>
  </svg>
  <div class="abs" role="img" aria-label="Portrait photo of a smiling bearded man in a light blue shirt" style="left:541px;top:68px;width:125px;height:125px;border-radius:58% 42% 48% 52% / 45% 40% 60% 55%;background:linear-gradient(160deg,#e2e2e2,#c9cfd6 70%,#8fb7cc)"></div>
</section>

<h2 class="abs cta-title">Do you have something to sell through us?</h2>
<a class="abs btn cta-btn">Sell your car now</a>

<footer class="abs footer">
  <div class="abs logo">AUTOVELKO</div>
  <p class="abs about">Lorem Ipsum is simply dummy text of the printing and typesetting industry. Lorem Ipsum has been the industry's standard dummy text ever since the 1500s, when an unknown...</p>
  <span class="abs more">Readmore</span>
  <div class="abs col contact" style="left:259px">
    <h3>Conatct info</h3>
    <ul>
      <li><svg width="8" height="10" viewBox="0 0 8 10"><path d="M4 0a4 4 0 0 1 4 4c0 3-4 6-4 6S0 7 0 4a4 4 0 0 1 4-4z" fill="#fff"/><circle cx="4" cy="4" r="1.5" fill="#cd1517"/></svg><span>Lorem Ipsum, Eastfield 10042<br>United States</span></li>
      <li><svg width="8" height="8" viewBox="0 0 10 10"><path d="M2 1l2 2-1 1.5a6 6 0 0 0 2.5 2.5L7 6l2 2-1.5 1.5C4.5 9 1 5.5.5 2.5z" fill="#fff"/></svg>1-800-555-0142</li>
      <li><svg width="8" height="7" viewBox="0 0 10 8"><rect width="10" height="8" rx="1" fill="#fff"/><path d="M0 1l5 3.5L10 1" stroke="#cd1517" fill="none"/></svg>info@velkomail.com</li>
      <li><svg width="8" height="8" viewBox="0 0 10 10"><circle cx="5" cy="5" r="4.5" fill="none" stroke="#fff"/><path d="M.5 5h9M5 .5v9" stroke="#fff" stroke-width=".8"/></svg>Live location</li>
    </ul>
  </div>
  <div class="abs col links" style="left:423px">
    <h3>Quick Link</h3>
    <ul><li>Home</li><li>What we do</li><li>Sign in</li><li>Dealership Login</li><li>Contact Us</li></ul>
  </div>
  <div class="abs col touch" style="left:539px">
    <h3>Stay In Touch</h3>
    <p>Subscribe to our newsletter and<br>stay updated</p>
    <div class="field"><i></i>Your email address*</div>
    <div class="btn submit">Submit</div>
  </div>
</footer>
<div class="abs bottom">
  <p>© 2024 AutoVelko. All Right Reserved</p>
  <div class="social"><span></span><span></span><span class="active"></span><span></span></div>
</div>

</body>
</html>
```